" 6920-6/01 - contabilidade 8599-6/03  - treinamento em informática 8599-6/99 - outros cursos 6209-1/00 - suporte técnico, manutençao e outros serviços  em tecnologia da informaçao (desde que realizados no estabelecimento do optante) 9511-8/00 - reparaçao e manutençao de computadores e de equipamentos periféricos 6201-5-00 - DESENVOLVIMENTO DE APLICATIVO INFORMATICO SOB ENCOMENDA 6202-3-00 - DESENVOLVIMENTO E LICENCIAMENTO DE PROGRAMAS DE COMPUTADOR CUSTOMIZAVEIS REVISAO FISCAL A partir da análise de notas fiscais, livros e demais documentos inerentes a área fiscal, verificamos a adequaçao de todos os procedimentos para a apuraçao e o recolhimentos dos tributos, apontando eventuais desvios de procedimentos e indicando as melhores soluçoes para reduzir os riscos. LEVANTAMENTO DE CRÉDITOS Através de revisao de documentos e procedimentos adotados no passado, realizamos um levantamento detalhado de todos os possíveis créditos fiscais e os métodos necessários para a sua compensaçao ou restituiçao. Os trabalhos sao realizados com visao contábil e legal, de forma a atender todas as necessidades do cliente. PLANEJAMENTO TRIBUTARIO O planejamento tem como objetivo orientar em todas as operaçoes fiscais, expandindo a visao do cliente para todas as questoes tributárias. Assim, visa reduzir a carga tributária encontrada, adotando diversas opçoes fiscais de acordo com os limites legais. CURSOS, PALESTRAS E TREINAMENTOS Ministramos diversos cursos voltados para a área tributária, além de realizar treinamentos específicos e direcionados a cada cliente, visando melhorar o desempenho do setor fiscal. As palestras tratam de assuntos diversificados e atuais, sendo realizadas por profissionais capacitados e com vasta experiência na área. "

```html
<!DOCTYPE html>
<html lang="pt-BR">
<head>
<meta charset="utf-8">
<title>Contavia – Papelaria</title>
<link rel="stylesheet" href="https://fonts.googleapis.com/css2?family=Poppins:wght@400;500&display=swap">
<style>
  :root {
    --teal: #3e8e94;
    --teal-dark: #347c82;
    --orange: #f08a1d;
    --paper: #ffffff;
    --ink: #6f7477;
    --rule: #c9cccd;
    --ground: #ecebe8;
    --faint: #eeeeee;
  }
  * { box-sizing: border-box; margin: 0; padding: 0; }
  html, body { width: 1200px; height: 1200px; overflow: hidden; }
  body {
    position: relative;
    background: var(--ground);
    font-family: "Poppins", sans-serif;
    color: var(--ink);
  }
  .piece { position: absolute; background: var(--paper); box-shadow: 0 2px 6px rgba(0,0,0,.12); overflow: hidden; }

  /* brand lockup */
  .brand { display: flex; align-items: center; gap: .35em; }
  .brand-dot { width: 1.05em; height: 1.05em; border-radius: 50%; background: var(--orange); flex: none; }
  .brand-text { display: flex; flex-direction: column; line-height: 1; }
  .brand-name { color: var(--teal); font-weight: 500; letter-spacing: -.01em; }
  .brand-tag { font-size: .3em; color: var(--ink); letter-spacing: .08em; margin-top: .25em; }

  .fine { font-size: 6px; line-height: 1.5; color: var(--ink); text-align: center; }

  /* folder */
  .folder { left: 30px; top: 30px; width: 460px; height: 520px; background: none; box-shadow: none; }
  .folder-cover { position: absolute; left: 0; top: 0; width: 230px; height: 520px; background: var(--paper); box-shadow: 0 2px 6px rgba(0,0,0,.12); }
  .folder-cover .brand { position: absolute; left: 28px; top: 370px; font-size: 30px; }
  .folder-cover .fine { position: absolute; left: 10px; right: 10px; bottom: 30px; }
  .folder-inside { position: absolute; left: 230px; top: 0; width: 230px; height: 520px; background: var(--teal); box-shadow: 0 2px 6px rgba(0,0,0,.12); }
  .folder-inside::before { content: ""; position: absolute; left: 0; right: 0; top: 0; height: 34px; background: var(--orange); }

  /* notepad */
  .notepad { left: 520px; top: 30px; width: 300px; height: 400px; }
  .notepad .brand { position: absolute; left: 22px; top: 18px; font-size: 18px; }
  .notepad-lines { position: absolute; left: 22px; right: 22px; top: 62px; height: 260px;
    background: repeating-linear-gradient(to bottom, transparent 0 11px, var(--rule) 11px 12px); }
  .notepad-date { position: absolute; right: 60px; top: 336px; font-size: 7px; }
  .notepad-date::after { content: ""; display: inline-block; width: 40px; border-bottom: 1px solid var(--rule); margin-left: 4px; }
  .notepad-foot { position: absolute; left: 0; right: 0; bottom: 0; height: 34px; background: var(--teal); padding-top: 8px; }
  .notepad-foot .fine { color: #fff; }

  /* letterhead */
  .letterhead { left: 850px; top: 30px; width: 320px; height: 440px; }
  .letterhead .brand { position: absolute; left: 22px; top: 18px; font-size: 18px; }
  .letterhead-mark { position: absolute; left: 70px; top: 95px; width: 230px; height: 230px; border-radius: 50%; background: var(--faint); }
  .letterhead-foot { position: absolute; left: 0; right: 0; bottom: 0; height: 34px; background: var(--teal); padding-top: 8px; }
  .letterhead-foot .fine { color: #fff; }

  /* small envelope */
  .envelope-small { left: 520px; top: 450px; width: 310px; height: 150px; }
  .envelope-small::after { content: ""; position: absolute; right: 0; top: 0; bottom: 0; width: 8px; background: var(--orange); }
  .envelope-small .brand { position: absolute; left: 88px; top: 42px; font-size: 24px; }
  .envelope-small .fine { position: absolute; left: 20px; right: 20px; top: 108px; }

  /* business cards */
  .card-front { left: 30px; top: 620px; width: 560px; height: 310px; }
  .card-front::before { content: ""; position: absolute; left: 0; top: 0; bottom: 0; width: 16px; background: var(--teal); }
  .card-front .brand { position: absolute; left: 100px; top: 110px; font-size: 64px; }

  .card-back { left: 610px; top: 620px; width: 560px; height: 310px; background: var(--teal); color: #fff; }
  .card-back::after { content: ""; position: absolute; right: 0; top: 0; bottom: 0; width: 16px; background: var(--orange); }
  .card-back-mark { position: absolute; left: 36px; top: 105px; width: 90px; height: 90px; border-radius: 50%; background: #fff; }
  .card-back-info { position: absolute; left: 158px; top: 62px; font-size: 13px; line-height: 1.35; }
  .card-back-info .person { font-size: 19px; font-weight: 500; line-height: 1.1; }
  .card-back-info .role { font-size: 12px; margin-bottom: 12px; }
  .card-back-info .gap { margin-top: 12px; }

  /* long envelope */
  .envelope-long { left: 30px; top: 960px; width: 1140px; height: 200px; }
  .envelope-long::before { content: ""; position: absolute; left: 0; right: 0; top: 0; height: 6px; background: var(--orange); }
  .envelope-long .brand { position: absolute; left: 90px; top: 58px; font-size: 56px; }
  .envelope-long-panel { position: absolute; right: 0; top: 24px; bottom: 0; width: 470px; background: var(--teal);
    color: #fff; font-size: 13px; line-height: 1.4; text-align: center; display: flex; flex-direction: column; justify-content: center; }
</style>
</head>
<body>

  <section class="piece folder">
    <div class="folder-cover">
      <div class="brand">
        <span class="brand-dot"></span>
        <span class="brand-text"><span class="brand-name">Contavia</span><span class="brand-tag">Assessoria Empresarial</span></span>
      </div>
      <p class="fine">Av. Nome Sobrenome, 0000 - São Paulo<br>Fone (11) 5555-5555 - www.contavia.com.br</p>
    </div>
    <div class="folder-inside"></div>
  </section>

  <section class="piece notepad">
    <div class="brand">
      <span class="brand-dot"></span>
      <span class="brand-text"><span class="brand-name">Contavia</span><span class="brand-tag">Assessoria Empresarial</span></span>
    </div>
    <div class="notepad-lines"></div>
    <p class="notepad-date">Data</p>
    <div class="notepad-foot">
      <p class="fine">Av. Nome Sobrenome, 0000 - São Paulo<br>Fone (11) 5555-5555 - www.contavia.com.br</p>
    </div>
  </section>

  <section class="piece letterhead">
    <div class="brand">
      <span class="brand-dot"></span>
      <span class="brand-text"><span class="brand-name">Contavia</span><span class="brand-tag">Assessoria Empresarial</span></span>
    </div>
    <div class="letterhead-mark"></div>
    <div class="letterhead-foot">
      <p class="fine">Av. Nome Sobrenome, 0000 - São Paulo<br>Fone (11) 5555-5555 - www.contavia.com.br</p>
    </div>
  </section>

  <section class="piece envelope-small">
    <div class="brand">
      <span class="brand-dot"></span>
      <span class="brand-text"><span class="brand-name">Contavia</span><span class="brand-tag">Assessoria Empresarial</span></span>
    </div>
    <p class="fine">Av. Nome Sobrenome, 0000 - São Paulo<br>Fone (11) 5555-5555 - www.contavia.com.br</p>
  </section>

  <section class="piece card-front">
    <div class="brand">
      <span class="brand-dot"></span>
      <span class="brand-text"><span class="brand-name">Contavia</span><span class="brand-tag">Assessoria Empresarial</span></span>
    </div>
  </section>

  <section class="piece card-back">
    <div class="card-back-mark"></div>
    <div class="card-back-info">
      <p class="person">Nome Sobrenome</p>
      <p class="role">Função</p>
      <p>nome@contavia.com.br</p>
      <p>Cel.: (11) 5555-5555</p>
      <p class="gap">Av. Nome Sobrenome, 0000</p>
      <p>CEP: 11000-000 - São Paulo - SP</p>
      <p>Fone/Fax: (11) 5555-5555</p>
      <p>www.contavia.com.br</p>
    </div>
  </section>

  <section class="piece envelope-long">
    <div class="brand">
      <span class="brand-dot"></span>
      <span class="brand-text"><span class="brand-name">Contavia</span><span class="brand-tag">Assessoria Empresarial</span></span>
    </div>
    <div class="envelope-long-panel">
      <p>Av. Nome Sobrenome, 0000 - Bairro Nome</p>
      <p>CEP: 11000-000 - São Paulo - SP</p>
      <p>Fone/Fax: (11) 5555-5555 - www.contavia.com.br</p>
    </div>
  </section>

</body>
</html>
```